A3 Menus for new international restaurant in Singapore.

Looking for new A3 menu design for indoor & outdoor (beautiful garden and trees) restaurant that caters for expat and local families. International menu, cool jazz vibe, great for couples and families. Restaurant called Fern Quay Commons. I have attached some of the logos we use. Will consider black and white or color options. Restaurant located on a hill where there were tin mines many years ago, hence the name and branding. Looking for three menus (1) Dinner (2) Lunch (3) weekend brunch.

Target Market(s)

Families, young couples and professionals.

Industry/Entity Type

Restaurant

Font styles to use
Serif
Sans Serif

Requirements
Must have
• All food layout on one side of A3, one for each attached menu. Also a space for drinks list on the back.
Nice to have
• Use some of the logo material we have attached.
Should not have

```html
<!DOCTYPE html>
<html lang="en">
<head>
<meta charset="utf-8">
<title>Fern Quay Commons – Weekendbrunch Menu</title>
<link rel="stylesheet" href="https://fonts.googleapis.com/css2?family=Libre+Baskerville:ital,wght@0,400;0,700;1,700&display=swap">
<style>
  :root{
    --ink:#231f20;
    --paper:#ffffff;
    --desc:#7a7a7a;
    --pink:#f4a7a3;
    --foliage:#f6e27a;
    --plant:#b9d3e6;
    --special-title:#a5df7c;
    --special-name:#f6e6a3;
    --hours-title:#a9c9e8;
    --hours-text:#f2df86;
  }
  *{margin:0;padding:0;box-sizing:border-box}
  html,body{width:848px;height:1200px;overflow:hidden;background:var(--paper)}
  body{font-family:"Libre Baskerville",Georgia,serif;color:var(--ink)}
  .menu{position:relative;width:848px;height:1200px;overflow:hidden;background:var(--paper)}
  .frame{position:absolute;background:var(--ink)}
  .frame-top{left:0;top:0;width:848px;height:78px}
  .frame-left{left:0;top:0;width:22px;height:1200px}
  .frame-right{right:0;top:0;width:22px;height:1200px}
  .frame-bottom{left:0;bottom:0;width:848px;height:28px}
  .menu-title{position:absolute;left:322px;top:12px;font-size:44px;font-weight:400;color:var(--paper);letter-spacing:.3px}
  .brand{position:absolute;left:34px;top:14px;width:250px;height:226px;background:var(--paper);padding:18px 14px;display:flex;flex-direction:column;justify-content:center}
  .brand-name{font-size:40px;line-height:46px;font-weight:700;color:var(--ink)}
  .foliage{position:absolute;left:240px;top:170px;width:580px;height:560px;border-radius:50%;
    background:radial-gradient(ellipse at center,rgba(246,226,122,.55) 0%,rgba(246,226,122,.3) 50%,rgba(246,226,122,0) 72%)}
  .plant{position:absolute;left:40px;top:900px;width:230px;height:270px;
    background:radial-gradient(ellipse at 50% 80%,rgba(185,211,230,.55) 0%,rgba(185,211,230,.2) 55%,rgba(185,211,230,0) 75%)}
  .section-band{position:absolute;left:30px;top:265px;width:376px;height:50px;background:var(--pink);padding:12px 0 0 18px;font-size:23px;font-weight:700;letter-spacing:.3px}
  .mug{position:absolute;left:330px;top:244px;width:62px;height:64px;border-radius:8px 8px 22px 22px;background:var(--ink)}
  .item{position:absolute;width:340px}
  .left .item{left:45px}
  .right .item{left:445px;width:337px}
  .line{display:flex;align-items:baseline;font-size:14.5px;font-weight:700;line-height:20px}
  .line > span:first-child{white-space:nowrap}
  .line.tight{font-size:13px;letter-spacing:-.3px}
  .leader{flex:1;min-width:6px;border-bottom:2px dotted var(--ink);margin:0 3px;transform:translateY(-4px)}
  .price{white-space:nowrap}
  .desc{color:var(--desc);font-size:13px;font-weight:700;line-height:19px;padding:3px 0 0 3px}
  .desc .price{color:var(--ink)}
  .plain-head{font-size:14.5px;font-weight:700;line-height:20px}
  .special{position:absolute;left:432px;top:582px;width:360px;height:126px;background:var(--ink);border-radius:18px;padding:12px 14px}
  .special-title{font-style:italic;font-weight:700;font-size:22px;color:var(--special-title);text-align:center;margin-bottom:8px}
  .special .line{color:var(--special-name)}
  .special .leader{border-color:var(--special-name)}
  .special .desc{color:var(--paper)}
  .hours{position:absolute;left:432px;top:1030px;width:416px;height:170px;background:var(--ink);border-radius:30px 0 0 0;padding:16px 0 0 0}
  .hours-title{color:var(--hours-title);font-size:20px;font-weight:700;text-align:center;margin:0 0 6px 0}
  .hours-row{display:grid;grid-template-columns:244px 1fr;color:var(--hours-text);font-size:19px;font-weight:700;line-height:30px;white-space:nowrap}
  .hours-row .day{text-align:right;padding-right:12px}
</style>
</head>
<body>
<main class="menu">
  <div class="foliage" role="img" aria-label="Soft yellow cross-hatched foliage illustration behind the menu"></div>
  <div class="plant" role="img" aria-label="Light blue line drawing of a leafy plant"></div>

  <div class="frame frame-top"></div>
  <div class="frame frame-left"></div>
  <div class="frame frame-right"></div>
  <div class="frame frame-bottom"></div>

  <h1 class="menu-title">Weekendbrunch Menu</h1>

  <div class="brand"><div class="brand-name">Fern Quay<br>Commons</div></div>

  <h2 class="section-band">WEEKENDBRUNCH</h2>
  <div class="mug" role="img" aria-label="Illustration of an enamel coffee mug"></div>

  <section class="left">
    <div class="item" style="top:332px"><div class="line tight"><span>Fern Quay Commons Muesli &amp; Yoghurt</span><span class="leader"></span><span class="price">$9.50</span></div><p class="desc">with fruit compote</p></div>
    <div class="item" style="top:390px"><div class="line"><span>Waffle</span><span class="leader"></span><span class="price">$14</span></div><p class="desc">served with mixed fruit, maple syrup and crushed nuts</p></div>
    <div class="item" style="top:467px"><div class="line"><span>Scrambled Eggs</span><span class="leader"></span><span class="price">$13.50</span></div><p class="desc">on sour dough toast, with roast tomato, portobello mushroom and chives</p></div>
    <div class="item" style="top:545px"><div class="line"><span>Baked Gypsy Eggs</span><span class="leader"></span><span class="price">$15.50</span></div><p class="desc">with rustic napolitano sauce, peas and diced pan-fried potato</p></div>
    <div class="item" style="top:618px"><div class="line"><span>Fern Quay Commons Eggs Benedict</span><span class="leader"></span><span class="price">$16</span></div><p class="desc">poached eggs served with either pulled pork or smoked salmon, served on toasted fresh brioche with paprika hollandaise and tomato confit</p></div>
    <div class="item" style="top:706px"><div class="line"><span>The Big Breakfast</span><span class="leader"></span><span class="price">$24</span></div><p class="desc">a choice of sunny-side up, over-easy or scrambled eggs, grilled bacon &amp; pork sausage, tomato, portobello mushroom, baked beans &amp; sourdough toast</p></div>
    <div class="item" style="top:810px"><div class="line"><span>Double Egg &amp; Bacon</span><span class="leader"></span><span class="price">$16</span></div><p class="desc">two eggs, fried or scrambled, bacon, roast tomato and sourdough toast</p></div>
    <div class="item" style="top:879px"><div class="line"><span>Classic Greek Salad</span><span class="leader"></span><span class="price">$14.50</span></div><p class="desc">with cherry tomatoes, feta, kalamata olives, green capsicum &amp; cucumber</p></div>
    <div class="item" style="top:955px"><div class="line"><span>Fern Quay Commons Garden Salad</span><span class="leader"></span><span class="price">$12</span></div><p class="desc">with mesclun leaves, cherry tomatoes, kalamata olives, shaved parmesan, classic vinaigrette and croutons</p></div>
    <div class="item" style="top:1047px"><div class="line"><span>Strigoli</span><span class="leader"></span><span class="price">$16</span></div><p class="desc">with beef ragubolognese</p></div>
  </section>

  <section class="right">
    <div class="item" style="top:100px"><div class="line"><span>Linguini</span><span class="leader"></span><span class="price">$17</span></div><p class="desc">in a light creamy carbonara sauce, with smoked pancetta</p></div>
    <div class="item" style="top:168px"><div class="line"><span>Rigatoni</span><span class="leader"></span><span class="price">add $3</span></div><p class="desc">with aglio, olio and pepperoncino <span class="price">$15</span> with prawns</p></div>
    <div class="item" style="top:240px"><div class="line"><span>Roast Beef Ciabatta</span><span class="leader"></span><span class="price">$17</span></div><p class="desc">with cheddar cheese, tomato and lettuce, served with fries</p></div>
    <div class="item" style="top:310px"><div class="line"><span>Fern Quay Commons Bangers &amp; Mash</span><span class="leader"></span><span class="price">$17</span></div><p class="desc">prime pork sausages, buttery mashed potato covered in onion &amp; cider gravy</p></div>
    <div class="item" style="top:378px"><div class="line"><span>Beer Battered Fish &amp; Chips</span><span class="leader"></span><span class="price">$17</span></div><p class="desc">with homemade tartar sauce and mushy peas</p></div>
    <div class="item" style="top:428px"><div class="line"><span>Fern Quay Commons Burger</span></div><p class="desc">200gms ground prime beef, in a homemade brioche bun with lettuce, tomato and mayo, and a side of fries<span class="price" style="float:right">$20</span></p></div>
    <div class="item" style="top:518px"><p class="desc">Top it with cheese or bacon or both<span class="price" style="float:right">add $2 for each</span></p></div>

    <div class="special">
      <h2 class="special-title">SUNDAY LUNCH SPECIAL</h2>
      <div class="line"><span>Fern Quay Commons Roast</span><span class="leader"></span><span class="price">$32.50</span></div>
      <p class="desc">roast beef sirloin with all the trimmings, yorkshire pudding and gravy</p>
    </div>

    <div class="item" style="top:732px"><p class="plain-head">Selection of freshly baked cakes and</p><div class="line"><span>tarts</span><span class="leader"></span><span class="price">each $9</span></div></div>
    <div class="item" style="top:786px"><div class="line"><span>Ice Cream</span><span class="leader"></span><span class="price">per scoop $5</span></div></div>
  </section>

  <aside class="hours">
    <h2 class="hours-title">Opening Hours:</h2>
    <div class="hours-row"><span class="day">Tuesday to Friday</span><span>10am to 12am</span></div>
    <div class="hours-row"><span class="day">Saturday and Sunday</span><span>9am to 12am</span></div>
    <div class="hours-row"><span class="day">Monday</span><span>Closed</span></div>
  </aside>
</main>
</body>
</html>
```